Voidcutter 5 Fundlaunch Graphic Design

My name is Tod, I design 3d-printable spaceships in 28mm scale. I have had four successful Fundlaunches, and for my fifth one, I want to take the graphic design of the campaign to the next level.
(see my last one here for an idea of what I am looking for, but better than the shitty graphics I myself made the last four times around: https://www.fundlaunch-example.com/projects/ironmoonworks/voidcutter-4-wyvern-modular-3d-printable-28mm-spaceship )

I am looking for a new sci-fi themed graphic design profile for the Fundlaunch page. This will include:
- Header design (I use images rather than fonts for titles) template in psd format that can have its text and colour changed easily by a third party, with a suitable sci-fi font.
- A sci-fi frames design for presenting 3D renders (with alpha channels) of miniatures, add-ons, stretch goals, framing photographic images, and presenting information, such as a chart of various campaign pledges
- Icons for locked and unlocked to be used in the frame above to show whether a stretch goal has been reached or is still being worked towards

I am looking for the creation of a series of photoshop templates that myself and my colleague can use to fill in the information needed for the campaign.

Thematically, the ship is designed with the same design language as the Halberdine from the Drift universe (see https://drift.wikihub-example.com/wiki/The_Drift_(TV) for a little more information and existing design profiles for the TV series, books and RPG), and I am looking to have a similar feel to this in my own graphic profile, without it being an outright copy. Something befitting a hard sci-fi universe.

The graphic profile must work well within the bounds of Fundlaunch's limitations and graphic profile. Graphics must be 680 pixels wide, and fit with the stark white background of Fundlaunch. We have no control over spacing between images (imagine it is a word press with sections), so there will be white space between them and any text, and or the next image, something to keep in mind.

Professional quality graphics, the use of colour to both categorise sections of the page (stretch goals, ship details, add-ons, pledges, etc) and lift otherwise mainly monotone renders, also would help work against the tedium of Fundlaunch's graphic profile.

The new ship looks like this:
https://www.filebox-example.com/s/9zkp2trwe8mnbqa/Final%20Form%20Front%20PDCs.png?dl=0

And you can see more images of WIP on my instagram below.
https://www.picshare-example.com/ironmoonworks3d/

Additional images can be provided.

Target Market(s)

Fundlaunch, 3d printing tabletop gamers

Font styles to use
Sans Serif

Requirements
Must have
• - Header design (I use images rather than fonts for titles) template in psd format that can have its text and colour changed easily by a third party, with a suitable sci-fi font. 680 px wide, height whatever looks good, but should be horizontal text.
- A sci-fi frame design template for presenting 3D renders (with alpha channels; 680 px wide, variable height) of miniatures, add-ons, stretch goals, framing photographic images, and presenting information, such as a chart of various campaign pledges
- Small Icons (less than 100×100, probably closer to 50×50) for locked and unlocked to be used in the frame above to show whether a stretch goal has been reached or is still being worked towards
Nice to have
• You could integrate the silhouette of the ship or features of the ship into the design, or follow a logical theme, such as a hangar bay, or having the graphics have RCS thrusters or something thematic like that.

The use of colour in the font/graphic to lift monotone renders is ideal
Should not have
• Should not be too gaudy or cluttered

```html
<!DOCTYPE html>
<html lang="en">
<head>
<meta charset="utf-8">
<title>Stretch Goals Header</title>
<link rel="stylesheet" href="https://fonts.googleapis.com/css2?family=Black+Ops+One&display=swap">
<style>
  :root {
    --page-bg: #ffffff;
    --panel-bg: #18191b;
    --accent-blue: #29a8e0;
    --glow-blue: #2a8fc8;
    --glow-amber: #8a5a2e;
    --title-tan: #a88560;
  }
  html, body {
    margin: 0;
    padding: 0;
    width: 1200px;
    height: 277px;
    overflow: hidden;
    background: var(--page-bg);
  }
  .header-banner {
    display: block;
    width: 1200px;
    height: 277px;
  }
  .section-title {
    font-family: "Black Ops One", "Arial Black", sans-serif;
    fill: var(--title-tan);
    font-size: 58px;
  }
</style>
</head>
<body>
<svg class="header-banner" viewBox="0 0 1200 277" xmlns="http://www.w3.org/2000/svg">
  <defs>
    <clipPath id="panel-clip">
      <rect x="128" y="89" width="938" height="114" rx="6"/>
    </clipPath>
    <radialGradient id="glow-blue" cx="0.5" cy="0.5" r="0.5">
      <stop offset="0" stop-color="var(--glow-blue)" stop-opacity="0.75"/>
      <stop offset="0.45" stop-color="var(--glow-blue)" stop-opacity="0.25"/>
      <stop offset="1" stop-color="var(--glow-blue)" stop-opacity="0"/>
    </radialGradient>
    <radialGradient id="glow-amber" cx="0.5" cy="0.5" r="0.5">
      <stop offset="0" stop-color="var(--glow-amber)" stop-opacity="0.8"/>
      <stop offset="0.5" stop-color="var(--glow-amber)" stop-opacity="0.25"/>
      <stop offset="1" stop-color="var(--glow-amber)" stop-opacity="0"/>
    </radialGradient>
    <linearGradient id="streak-blue" x1="0" x2="1">
      <stop offset="0" stop-color="var(--accent-blue)" stop-opacity="0"/>
      <stop offset="0.15" stop-color="var(--accent-blue)" stop-opacity="0.9"/>
      <stop offset="0.7" stop-color="var(--accent-blue)" stop-opacity="0.5"/>
      <stop offset="1" stop-color="var(--accent-blue)" stop-opacity="0"/>
    </linearGradient>
    <linearGradient id="streak-amber" x1="0" x2="1">
      <stop offset="0" stop-color="#b07a45" stop-opacity="0"/>
      <stop offset="0.2" stop-color="#b07a45" stop-opacity="0.9"/>
      <stop offset="0.75" stop-color="#b07a45" stop-opacity="0.5"/>
      <stop offset="1" stop-color="#b07a45" stop-opacity="0"/>
    </linearGradient>
  </defs>

  <!-- outer frame bracket -->
  <g class="frame-bracket" fill="none" stroke="var(--accent-blue)" stroke-width="1.2">
    <path d="M120 141 V83.5 H1013"/>
  </g>

  <!-- dark title panel -->
  <rect class="title-panel" x="128" y="89" width="938" height="114" rx="6" fill="var(--panel-bg)"/>

  <g class="panel-lighting" clip-path="url(#panel-clip)">
    <ellipse cx="357" cy="102" rx="90" ry="55" fill="url(#glow-blue)"/>
    <ellipse cx="262" cy="198" rx="95" ry="40" fill="url(#glow-amber)"/>
    <rect x="330" y="99.5" width="420" height="1" fill="url(#streak-blue)"/>
    <rect x="270" y="134.5" width="660" height="1" fill="url(#streak-blue)"/>
    <rect x="290" y="180.5" width="480" height="1.2" fill="url(#streak-amber)"/>
  </g>

  <!-- segmented indicator blocks -->
  <g class="indicator-blocks" fill="var(--accent-blue)">
    <rect x="156" y="73" width="34" height="22"/>
    <rect x="199" y="73" width="33" height="22"/>
    <rect x="242" y="73" width="26" height="22"/>
    <rect x="277" y="73" width="28" height="22"/>
    <rect x="329" y="73" width="17" height="22"/>
    <rect x="355" y="73" width="17" height="22"/>
    <rect x="404" y="73" width="6" height="22"/>
    <rect x="418" y="73" width="7" height="22"/>
    <rect x="439" y="73" width="6" height="22"/>
    <rect x="500" y="73" width="8" height="22"/>
    <rect x="514" y="73" width="7" height="22"/>
    <rect x="535" y="73" width="7" height="22"/>
  </g>

  <text class="section-title" x="160" y="172" textLength="656" lengthAdjust="spacingAndGlyphs">STRETCH GOALS</text>
</svg>
</body>
</html>
```